Feng shui business card for immigration law firm

Immigration law firm would like to create the business card based and look like the Green Card (lawful permanent resident card of USA). Attached please see the sample of American Green Card. The whole business card should be performed based on the FENG SHUI style: no sharp angles. Please delete all letters and fingerprint on the sample green card and put info the following order.

Target Market(s)

Immigration clients in USA

Industry/Entity Type

Business

Contact Information for Business Card

Immigration law firm would like to create the business card based and look like the Green Card (lawful permanent resident card of USA). Attached please see the sample of American Green Card. The whole business card should be performed based on the FENG SHUI style: no sharp angles. Please delete all letters on sample green card and put info the following order:

TOLAN BERIKSOVA, ESQ.
BERIKSOVA LAW GROUP, P.A.
PRACTICE LIMITED TO IMMIGRATION LAW

4370 WEST CORVINDALE PARK BOULVERD
SUITE #218
CORVINDALE PARK, FLORIDA 33174

PHONE: 754-555-0162
EMAIL: TBERIKSOVA@QUELMAIL.EXAMPLE
WEBSITE: WWW.ZORVEL-VISAHELP.EXAMPLE

The tips for the best business card
1. It is recommended to avoid using sharp points in the logo because such logos generate negative energy. Never use sharp and pointed element like spears, knives or swords in your logo.
2. One of the most essential elements in Feng Shui good flow and space which means that there should not be any obstruction, for example, there should not be any border around the card as it stop the energy flow.
3. Keep clear of clutter – Just like applying this feng shui concept to home and office, it should also be applied to designing your name card. Always keep your card as clean and concise as possible by removing all redundant information and put only relevant ones.
4. Name should not be placed in the center of the card because it cause stress and pressure to the owner.

Font styles to use
Other font styles liked:
• Garamond or Times New Roman

Requirements
Must have
• Feng shui business card

```html
<!DOCTYPE html>
<html lang="en">
<head>
<meta charset="utf-8">
<title>Beriksova Law Group business card</title>
<link href="https://fonts.googleapis.com/css2?family=EB+Garamond:wght@400;500&family=Open+Sans:wght@400;600&display=swap" rel="stylesheet">
<style>
  :root {
    --red: #e0202b;
    --white: #ffffff;
    --ink: #1c1c1c;
    --grey-line: #5a5a5a;
    --page: #e9e7e4;
    --serif: "EB Garamond", "Times New Roman", serif;
    --sans: "Open Sans", Arial, sans-serif;
  }
  * { box-sizing: border-box; margin: 0; padding: 0; }
  html, body { width: 1200px; height: 902px; overflow: hidden; background: var(--page); }
  .canvas { position: relative; width: 1200px; height: 902px; }
  .card {
    position: absolute; left: 250px; width: 700px; height: 400px;
    background: var(--white); border-radius: 14px; overflow: hidden;
    box-shadow: 0 6px 18px rgba(0,0,0,0.12);
  }
  .card-back { top: 31px; }
  .card-front { top: 471px; }

  /* back */
  .back-band {
    position: absolute; left: 0; right: 0; top: 110px; height: 150px; background: var(--red);
  }
  .back-mark {
    position: absolute; left: 0; right: 0; top: 110px; height: 150px;
    display: flex; align-items: center; justify-content: center; gap: 16px;
  }
  .mark-square { width: 46px; height: 46px; border-radius: 8px; }
  .back-mark .mark-square { background: var(--white); }
  .mark-name { font-family: var(--serif); font-weight: 500; letter-spacing: 2px; white-space: nowrap; }
  .back-mark .mark-name { color: var(--white); font-size: 40px; }
  .back-firm {
    position: absolute; left: 0; right: 0; top: 290px; text-align: center;
    font-family: var(--serif); color: var(--ink);
  }
  .back-firm .firm-name { font-size: 30px; letter-spacing: 1px; }
  .back-firm .firm-tagline { font-size: 25px; color: #444; }

  /* front */
  .front-mark {
    position: absolute; left: 40px; top: 112px; display: flex; align-items: center; gap: 10px;
  }
  .front-mark .mark-square { width: 30px; height: 30px; background: var(--red); border-radius: 6px; }
  .front-mark .mark-name { color: var(--red); font-size: 24px; }
  .front-firm { position: absolute; left: 290px; top: 36px; font-family: var(--serif); color: var(--ink); }
  .front-firm .firm-name { font-size: 27px; letter-spacing: 0.5px; white-space: nowrap; }
  .front-firm .firm-tagline { font-size: 23px; color: #333; white-space: nowrap; }
  .divider { position: absolute; left: 410px; top: 140px; width: 2px; height: 100px; background: var(--ink); }
  .person { position: absolute; right: 305px; top: 180px; text-align: right; font-family: var(--sans); color: var(--ink); }
  .person-name { font-size: 26px; font-weight: 600; line-height: 1.15; white-space: nowrap; }
  .person-title { font-size: 21px; font-weight: 600; }
  .contact { position: absolute; left: 424px; top: 148px; font-family: var(--sans); color: var(--ink); font-size: 16px; line-height: 30px; }
  .contact-row { display: flex; align-items: center; gap: 7px; white-space: nowrap; }
  .contact-row svg { width: 16px; height: 16px; flex: none; }
  .swoosh { position: absolute; left: 0; top: 0; width: 700px; height: 400px; }
  .office {
    position: absolute; left: 0; right: 0; top: 314px; text-align: center;
    font-family: var(--sans); color: var(--white); font-size: 17px; line-height: 26px;
    white-space: nowrap;
  }
</style>
</head>
<body>
<main class="canvas">
  <section class="card card-back" aria-label="Card back">
    <div class="back-band"></div>
    <div class="back-mark">
      <span class="mark-square"></span>
      <span class="mark-name">BERIKSOVA</span>
    </div>
    <div class="back-firm">
      <p class="firm-name">BERIKSOVA LAW GROUP, P.A.</p>
      <p class="firm-tagline">Practice Limited to Immigration Law</p>
    </div>
  </section>

  <section class="card card-front" aria-label="Card front">
    <svg class="swoosh" viewBox="0 0 700 400" aria-hidden="true">
      <path d="M0 296 Q 360 290 700 236" fill="none" stroke="var(--grey-line)" stroke-width="3"/>
      <path d="M0 400 L0 306 Q 360 300 700 246 L700 400 Z" fill="var(--red)"/>
    </svg>
    <div class="front-mark">
      <span class="mark-square"></span>
      <span class="mark-name">BERIKSOVA</span>
    </div>
    <div class="front-firm">
      <p class="firm-name">BERIKSOVA LAW GROUP, P.A.</p>
      <p class="firm-tagline">Practice Limited to Immigration Law</p>
    </div>
    <div class="person">
      <p class="person-name">Tolan Beriksova</p>
      <p class="person-title">Esq</p>
    </div>
    <div class="divider"></div>
    <div class="contact">
      <p class="contact-row">
        <svg viewBox="0 0 16 16" aria-hidden="true"><rect width="16" height="16" rx="3" fill="var(--ink)"/><path d="M5 3.5c-1 .5-1.6 1.4-1 3 .8 2 2.4 3.8 4.5 5 1.3.7 2.3.3 2.9-.6l-1.7-1.6-1.2.6C7.5 9.4 6.7 8.5 6.2 7.5l.8-1.1z" fill="var(--white)"/></svg>
        754-555-0162
      </p>
      <p class="contact-row">
        <svg viewBox="0 0 16 16" aria-hidden="true"><rect width="16" height="16" rx="3" fill="var(--ink)"/><rect x="3" y="4.5" width="10" height="7" rx="1" fill="var(--white)"/><path d="M3.5 5l4.5 3.5L12.5 5" fill="none" stroke="var(--ink)" stroke-width="1"/></svg>
        tberiksova@quelmail.example
      </p>
    </div>
    <div class="office">
      <p>www.zorvel-visahelp.example</p>
      <p>4370 West Corvindale Park Boulverd Suite #218</p>
      <p>Corvindale Park, Florida 33174</p>
    </div>
  </section>
</main>
</body>
</html>
```